Photoshop Templates for Instagram, x 2

A Square template to reuse that is on brand.

It will involve an image and text of between 3 and 10 words.
I would like 2 separate contrasting images to use interchangeably

In the files I have added some of the images that I have been using, as well as the home page of my website that is currently being developed.

The on brand would be very recognisable with the website.

Requirements
Must have
• Must be similar in feel to the home page.

Must be simple to to change image and and text in the template

I would like 2 designs. Both similar, but contrasting

The square images show the look that I have been using (created by myself, so I'm sure these can be massively improved upon)

```html
<!DOCTYPE html>
<html lang="en">
<head>
<meta charset="utf-8">
<title>Quote Post Templates</title>
<link rel="stylesheet" href="https://fonts.googleapis.com/css2?family=Josefin+Sans:wght@300;700&display=swap">
<style>
  :root {
    --ink: #000000;
    --paper: #ffffff;
    --accent: #0aa3e6;
    --photo-light: #3a4a78;
    --photo-dark: #1b2140;
    --type: "Josefin Sans", sans-serif;
  }
  * { margin: 0; padding: 0; box-sizing: border-box; }
  html, body {
    width: 1200px; height: 596px; overflow: hidden;
    background: var(--paper);
    font-family: var(--type);
  }
  .post {
    position: absolute; top: 0;
    width: 596px; height: 596px;
    background: var(--ink);
    overflow: hidden;
  }
  .post--portrait { left: 0; }
  .post--chevron { left: 604px; }

  .photo-slot {
    position: absolute;
    background: linear-gradient(160deg, var(--photo-light) 0%, var(--photo-dark) 100%);
  }
  .post--portrait .photo-slot { left: 0; top: 0; width: 287px; height: 548px; }
  .post--chevron .photo-slot {
    left: 0; top: 0; width: 596px; height: 337px;
    clip-path: polygon(0 0, 596px 0, 596px 21px, 296px 316px, 0 21px);
  }

  .shapes { position: absolute; inset: 0; }

  .quote { position: absolute; text-align: center; color: var(--paper); font-weight: 700; text-transform: uppercase; line-height: 1; }
  .quote .hl { color: var(--accent); }
  .line { position: absolute; left: 0; right: 0; white-space: nowrap; }

  .author {
    position: absolute;
    color: var(--paper); font-weight: 300; text-transform: uppercase;
    text-align: center; white-space: nowrap; line-height: 1;
  }

  .quote-card {
    position: absolute; left: 331px; top: 94px; width: 246px; height: 400px;
    border: 1px solid var(--paper);
  }
  .quote-card .quote { left: 0; right: 0; top: 0; }
  .quote-card .author { left: 0; right: 0; top: 362px; font-size: 18px; }

  .post--chevron .quote { left: 0; width: 596px; top: 0; }
  .post--chevron .line { font-size: 28px; }
  .post--chevron .author { left: 0; width: 596px; top: 523px; font-size: 19px; }
</style>
</head>
<body>

<section class="post post--portrait">
  <div class="photo-slot" role="img" aria-label="Photo of a footballer celebrating and pointing toward the viewer"></div>
  <svg class="shapes" width="596" height="596" viewBox="0 0 596 596">
    <rect x="288" y="262" width="16" height="302" fill="var(--accent)"/>
    <rect x="203" y="548" width="101" height="16" fill="var(--accent)"/>
  </svg>
  <div class="quote-card">
    <div class="quote">
      <span class="line" style="top:28px;font-size:33px">You can</span>
      <span class="line hl" style="top:69px;font-size:33px">Overcome</span>
      <span class="line hl" style="top:109px;font-size:33px">Anything,</span>
      <span class="line" style="top:146px;font-size:19px">If and only if you</span>
      <span class="line hl" style="top:182px;font-size:57px">Love</span>
      <span class="line" style="top:248px;font-size:33px">Something</span>
      <span class="line hl" style="top:298px;font-size:42px">Enough</span>
    </div>
    <p class="author">-Marco Delvane</p>
  </div>
</section>

<section class="post post--chevron">
  <div class="photo-slot" role="img" aria-label="Photo of a footballer celebrating and pointing toward the viewer"></div>
  <svg class="shapes" width="596" height="596" viewBox="0 0 596 596">
    <rect x="24.5" y="157.5" width="378" height="398" fill="none" stroke="var(--paper)" stroke-width="1"/>
    <rect x="202.5" y="505.5" width="420" height="120" fill="none" stroke="var(--paper)" stroke-width="1"/>
    <polygon points="114,155 135,155 296,313 457,155 478,155 296,337" fill="var(--accent)"/>
  </svg>
  <div class="quote">
    <span class="line" style="top:371px">You can <span class="hl">Overcome Anything,</span></span>
    <span class="line" style="top:418px">If and only if you</span>
    <span class="line" style="top:465px"><span class="hl">Love</span> Something <span class="hl">Enough</span></span>
  </div>
  <p class="author">-Marco Delvane</p>
</section>

</body>
</html>
```